Brontaro Web Site

Redesigned web site for Brontaro Ltd (www.brontaro-example.co.uk). This is to feature new logo (attached). Brontaro Ltd is a company which specialises in Geographic Information Systems and Geographic data - we call ourselves GIS Data Specialists. We are looking for something which conveys our professionalism and our experience. There will be more pages than on the current Brontaro website. There will be: Home, Data Migration, Data Cleansing & Validation, Data Analysis, Data Maintenance, Data Quality and an About Us page. All these should be accessible from each page on the website.
Updates
I didn't really think to say that the content of the web site is going to change from the current one we have. There will be more pages than on the current one. They will be: Home, Data Migration, Data Cleansing & Validation, Data Analysis, Data Maintenance, Data Quality and an About Us page. All these should be accessible from each page on the website. I didn't really think through the fact that the number of pages / areas to access can influence the layout of the site, sorry.
Target Market(s)
Utility Companies (e.g. telecommunications providers, energy companies), local government.
Industry/Entity Type
It Company
Look and feel

```html
<!DOCTYPE html>
<html lang="en">
<head>
<meta charset="utf-8">
<title>Brontaro – GIS Data Specialists</title>
<link rel="stylesheet" href="https://fonts.googleapis.com/css2?family=Source+Sans+3:wght@400&family=PT+Sans+Narrow:wght@400&display=swap">
<style>
  :root {
    --page-bg: #d4f7f3;
    --panel-top: #c6ebe7;
    --panel-light: #ffffff;
    --panel-teal: #82d5cd;
    --panel-bottom: #d6f6f2;
    --text: #7b7b7b;
    --heading: #777777;
    --nav-active: #6f6f6f;
    --nav: #b3b3b3;
    --divider: #a8ddd7;
    --brand: #7d7d7d;
    --brand-dot: #86d8cf;
    --lines: #e6d3b3;
  }
  * { margin: 0; padding: 0; box-sizing: border-box; }
  html, body { width: 1200px; height: 900px; overflow: hidden; }
  body {
    position: relative;
    background: var(--page-bg);
    font-family: "Source Sans 3", "Myriad Pro", sans-serif;
    color: var(--text);
  }
  .side-decor {
    position: absolute;
    top: 130px;
    height: 420px;
    width: 260px;
    opacity: 0.55;
  }
  .side-decor--left {
    left: 0;
    background: radial-gradient(ellipse at 0% 50%, var(--lines) 0%, transparent 70%);
  }
  .side-decor--right {
    right: 0;
    background: radial-gradient(ellipse at 100% 50%, var(--lines) 0%, transparent 70%);
  }
  .brand {
    position: absolute;
    left: 140px;
    top: 58px;
    display: flex;
    align-items: center;
    gap: 22px;
  }
  .brand__dot {
    width: 52px;
    height: 52px;
    border-radius: 50%;
    background: var(--brand-dot);
  }
  .brand__name {
    font-size: 48px;
    font-weight: 400;
    color: var(--brand);
    letter-spacing: 0.5px;
  }
  .panel {
    position: absolute;
    left: 132px;
    top: 170px;
    width: 936px;
    height: 730px;
    background: linear-gradient(to bottom,
      var(--panel-top) 0%,
      var(--panel-light) 23%,
      var(--panel-light) 27%,
      #c5ece8 48%,
      var(--panel-teal) 69%,
      #a6e2dc 82%,
      var(--panel-bottom) 100%);
    box-shadow: 0 0 24px rgba(120, 190, 182, 0.35);
  }
  .nav {
    position: absolute;
    left: 43px;
    top: 70px;
    width: 120px;
    list-style: none;
    font-family: "PT Sans Narrow", "Myriad Pro Condensed", sans-serif;
    font-size: 14px;
    line-height: 20px;
  }
  .nav li { margin-bottom: 19px; }
  .nav a { color: var(--nav); text-decoration: none; }
  .nav a.is-current { color: var(--nav-active); }
  .nav-divider {
    position: absolute;
    left: 160px;
    top: 30px;
    width: 2px;
    height: 500px;
    background: linear-gradient(to bottom, transparent, var(--divider) 15%, var(--divider) 85%, transparent);
  }
  .content {
    position: absolute;
    left: 209px;
    top: 50px;
    width: 665px;
  }
  .content h1 {
    font-size: 28px;
    font-weight: 400;
    color: var(--heading);
    line-height: 36px;
    margin-bottom: 6px;
  }
  .content p {
    font-size: 17.5px;
    line-height: 22.6px;
    margin-bottom: 22.6px;
  }
</style>
</head>
<body>
  <div class="side-decor side-decor--left" role="img" aria-label="Fine curved contour lines fanning across the page edge"></div>
  <div class="side-decor side-decor--right" role="img" aria-label="Fine curved contour lines fanning across the page edge"></div>

  <header class="brand">
    <span class="brand__dot"></span>
    <span class="brand__name">Brontaro</span>
  </header>

  <main class="panel">
    <ul class="nav">
      <li><a class="is-current" href="#">Home</a></li>
      <li><a href="#">Data Migration</a></li>
      <li><a href="#">Data Cleaning &amp;<br>Validation</a></li>
      <li><a href="#">Data Analysis</a></li>
      <li><a href="#">Data Maintenance</a></li>
      <li><a href="#">Data Quality</a></li>
      <li><a href="#">About Us</a></li>
    </ul>
    <div class="nav-divider"></div>

    <section class="content">
      <h1>Welcome to Brontaro</h1>
      <p>Brontaro was founded in 1994 by a group of geospatial software engineers that recognised the significant value that data, and the systems used to store and analyse this data, could bring to business.</p>
      <p>Our Customers: We have worked with over 200 companies in a myriad of market sectors - from utilities, local and central government, oil and gas, to many spheres of the marine industry.</p>
      <p>Our Pedigree: We provide a vast bank of knowledge and experience to offer an all encompassing service. This ensures that you, as a customer, reap the maximum benefits from your data and systems through utilising a combination of our skilled consultants, analysts and developers that will work with you and your requirements to help achieve your business objectives.</p>
      <p>Our People: We have a wide ranging skill set including PACE 2 qualified Project Managers, fully qualified Software Developers and Experienced Data Consultants.</p>
    </section>
  </main>
</body>
</html>
```